Label for new gin: Kliff7 - Distilled Gin

Artistic label with local elements for new gin brand.
Dunes, lighthouses, sea, seagulls, ships.
Fresh lemon gin with fine juniper notes. Manufactured directly on the Baltic Sea in Warnemünde. Should be scalable. 4x6inch or larger.
Motifs put together artistically. Photos of the place in the attachment. The name of the gin comes from the beach entrance 3 (hence dune 3). A dune stalk (blue oat) is in the bottle. Bottle will be a clear glass apothecary bottle 500ml.
Updates

Niedrige Design-Qualität

Target Market(s)

spirits

Industry/Entity Type

Getränke

Font styles to use
Decorative
Script

Colors

Designer to choose colors to be used in the design.

Requirements
Must have
• Sketch, Handdrawn Style /// 500ml, 41% vol Alc "Made by QMTO GmbH Farnstieg 22a Roggentin" "Bottled in Warnemünde" "Kliff7" "Distilled Gin" "Inspired by the sea"

```html
<!DOCTYPE html>
<html lang="de">
<head>
<meta charset="utf-8">
<title>Kliff7 Distilled Gin – Labels</title>
<link rel="stylesheet" href="https://fonts.googleapis.com/css2?family=Cinzel:wght@500&family=Cinzel+Decorative:wght@900&family=Ultra&family=Kaushan+Script&family=Oswald:wght@400;500&family=Libre+Caslon+Text&display=swap">
<style>
  :root {
    --page: #fbfbf6;
    --label: #e6e9eb;
    --ink: #1d1d1d;
    --gold: #8a7b1f;
    --band: #2a2a2a;
    --band-text: #f2f2f2;
    --sketch-light: #e9ebec;
    --sketch-mid: #cdd0d2;
    --sketch-dark: #b4b8bb;
  }
  * { margin: 0; padding: 0; box-sizing: border-box; }
  html, body { width: 1200px; height: 1200px; overflow: hidden; }
  body { background: var(--page); position: relative; }

  .label {
    position: absolute;
    top: 260px;
    width: 500px;
    height: 680px;
    background: var(--label);
    box-shadow: 0 6px 24px rgba(0,0,0,0.08);
    overflow: hidden;
  }
  .label--dunes { left: 67px; }
  .label--harbour { left: 633px; }

  .label__scene {
    position: absolute;
    left: 0; right: 0;
    top: 220px; height: 370px;
  }
  .label--dunes .label__scene {
    background:
      radial-gradient(120% 40% at 30% 45%, rgba(180,184,187,0.45) 0%, rgba(180,184,187,0) 60%),
      radial-gradient(90% 35% at 80% 60%, rgba(180,184,187,0.5) 0%, rgba(180,184,187,0) 60%),
      linear-gradient(180deg, rgba(233,235,236,0) 0%, var(--sketch-light) 20%, var(--sketch-mid) 70%, var(--sketch-dark) 100%);
  }
  .label--harbour .label__scene {
    background:
      radial-gradient(18% 70% at 86% 45%, rgba(180,184,187,0.6) 0%, rgba(180,184,187,0) 70%),
      radial-gradient(80% 25% at 70% 88%, rgba(170,174,177,0.55) 0%, rgba(170,174,177,0) 70%),
      linear-gradient(180deg, rgba(233,235,236,0) 0%, var(--sketch-light) 35%, #d6d9db 55%, var(--sketch-mid) 100%);
  }

  .label__tagline {
    position: absolute; top: 68px; left: 0; right: 0;
    text-align: center;
    font-family: "Cinzel", serif;
    font-weight: 500;
    font-size: 24px;
    line-height: 28px;
    letter-spacing: 2px;
    color: var(--gold);
  }
  .label__name {
    position: absolute; top: 180px; left: 0; right: 0;
    text-align: center;
    font-family: "Cinzel Decorative", serif;
    font-weight: 900;
    font-size: 92px;
    line-height: 110px;
    color: var(--ink);
  }
  .label__meta {
    position: absolute; top: 335px; left: 44px; right: 44px;
    display: flex; align-items: center; justify-content: space-between;
  }
  .meta-stamp {
    font-family: "Libre Caslon Text", serif;
    text-align: center;
    color: var(--ink);
    line-height: 1.05;
  }
  .meta-stamp__big { font-size: 19px; }
  .meta-stamp__small { font-size: 12px; letter-spacing: 1px; }
  .label__product {
    font-family: "Kaushan Script", cursive;
    font-size: 44px;
    color: var(--ink);
  }
  .label__origin {
    position: absolute; top: 455px; left: 0; right: 0;
    text-align: center;
    font-family: "Ultra", serif;
    font-size: 25px;
    line-height: 36px;
    letter-spacing: 1.5px;
    color: var(--ink);
  }
  .label__motto {
    position: absolute; top: 528px; left: 0; right: 0;
    text-align: center;
    font-family: "Kaushan Script", cursive;
    font-size: 21px;
    color: var(--gold);
  }

  .label__band {
    position: absolute; left: 0; bottom: 0;
    width: 500px; height: 100px;
  }
  .band__content {
    position: absolute; left: 0; right: 0; top: 14px; height: 74px;
    display: flex; align-items: center; justify-content: space-between;
    padding: 0 32px;
    font-family: "Oswald", sans-serif;
    color: var(--band-text);
  }
  .band__volume { font-size: 17px; line-height: 22px; text-align: center; font-weight: 500; }
  .band__maker { font-size: 11.5px; line-height: 17px; text-align: center; letter-spacing: 0.3px; }
  .band__dots { display: flex; align-items: center; gap: 14px; }
  .band__dots span { display: block; border-radius: 50%; background: var(--band-text); }
  .dot-s { width: 9px; height: 9px; }
  .dot-m { width: 13px; height: 13px; }
  .dot-l { width: 19px; height: 19px; }
</style>
</head>
<body>

  <svg width="0" height="0" style="position:absolute">
    <defs>
      <pattern id="sawtooth-top" width="8" height="6" patternUnits="userSpaceOnUse">
        <path d="M0 6 L4 0 L8 6 Z" fill="#2a2a2a"/>
      </pattern>
      <pattern id="sawtooth-bottom" width="8" height="6" patternUnits="userSpaceOnUse">
        <path d="M0 0 L4 6 L8 0 Z" fill="#2a2a2a"/>
      </pattern>
    </defs>
  </svg>

  <section class="label label--dunes">
    <div class="label__scene" role="img" aria-label="Hand-drawn pencil sketch of Baltic sand dunes with beach grass and a pebbled shore"></div>
    <div class="label__tagline">SMALL BATCH<br>CRAFTED</div>
    <div class="label__name">KLIFF7</div>
    <div class="label__meta">
      <div class="meta-stamp"><div class="meta-stamp__big">EST</div><div class="meta-stamp__small">2021</div></div>
      <div class="label__product">Distilled Gin</div>
      <div class="meta-stamp"><div class="meta-stamp__big">80</div><div class="meta-stamp__small">PROOF</div></div>
    </div>
    <div class="label__origin">BOTTLED IN<br>WARNEMUNDE</div>
    <div class="label__motto">Inspired By The Sea</div>
    <div class="label__band">
      <svg width="500" height="100" aria-hidden="true">
        <rect x="0" y="6" width="500" height="88" fill="#2a2a2a"/>
        <rect x="0" y="0" width="500" height="6" fill="url(#sawtooth-top)"/>
        <rect x="0" y="94" width="500" height="6" fill="url(#sawtooth-bottom)"/>
      </svg>
      <div class="band__content">
        <div class="band__volume">500ML<br>41% VOL/ALC</div>
        <div class="band__dots"><span class="dot-s"></span><span class="dot-m"></span><span class="dot-l"></span><span class="dot-m"></span><span class="dot-s"></span></div>
        <div class="band__maker">MADE BY<br>QMTO GMBH FARNSTIEG<br>22A ROGGENTIN</div>
      </div>
    </div>
  </section>

  <section class="label label--harbour">
    <div class="label__scene" role="img" aria-label="Hand-drawn pencil sketch of the Warnemünde harbour with the lighthouse on the pier, a sailboat, the sea and rocks"></div>
    <div class="label__tagline">SMALL BATCH<br>CRAFTED</div>
    <div class="label__name">KLIFF7</div>
    <div class="label__meta">
      <div class="meta-stamp"><div class="meta-stamp__big">EST</div><div class="meta-stamp__small">2021</div></div>
      <div class="label__product">Distilled Gin</div>
      <div class="meta-stamp"><div class="meta-stamp__big">80</div><div class="meta-stamp__small">PROOF</div></div>
    </div>
    <div class="label__origin">BOTTLED IN<br>WARNEMUNDE</div>
    <div class="label__motto">Inspired By The Sea</div>
    <div class="label__band">
      <svg width="500" height="100" aria-hidden="true">
        <rect x="0" y="6" width="500" height="88" fill="#2a2a2a"/>
        <rect x="0" y="0" width="500" height="6" fill="url(#sawtooth-top)"/>
        <rect x="0" y="94" width="500" height="6" fill="url(#sawtooth-bottom)"/>
      </svg>
      <div class="band__content">
        <div class="band__volume">500ML<br>41% VOL/ALC</div>
        <div class="band__dots"><span class="dot-s"></span><span class="dot-m"></span><span class="dot-l"></span><span class="dot-m"></span><span class="dot-s"></span></div>
        <div class="band__maker">MADE BY<br>QMTO GMBH FARNSTIEG<br>22A ROGGENTIN</div>
      </div>
    </div>
  </section>

</body>
</html>
```